University of Corvale Brindle Saxophone Ensembles Concert

A poster advertising the concert for the Brindle Saxophone Ensembles (Saxophone Ensemble / 2 Saxophone Quartets). Concert date is Friday, April 19 at 8pm in the Tobias Wrenfield Concert Hall. Poster should be not "goofy" but not overly serious.

Target Market(s)

College Students/Fellow Music Students

Industry/Entity Type

Advertising

Requirements
Must have
• Must have..

1. Brindle Saxophone Ensembles from the Studios of Perry Halvorsen and Neil Dumont
2. Date
3. Time
4. Place

```html
<!DOCTYPE html>
<html lang="en">
<head>
<meta charset="utf-8">
<title>Brindle Saxophone Ensembles — Concert Poster</title>
<link rel="stylesheet" href="https://fonts.googleapis.com/css2?family=Lilita+One&family=Roboto+Condensed:wght@700&display=swap">
<style>
  :root {
    --sky-purple: #4a2a8a;
    --sky-mauve: #9a4a78;
    --sky-amber: #d6a24c;
    --sky-gold: #e6cc60;
    --brass-deep: #3e0c08;
    --brass-mid: #8a2a14;
    --brass-light: #c4602e;
    --title-yellow: #f7f200;
    --title-shadow: #4a3010;
    --info-white: #ffffff;
  }
  * { margin: 0; padding: 0; box-sizing: border-box; }
  html, body { width: 900px; height: 1200px; overflow: hidden; }
  .poster {
    position: relative;
    width: 900px;
    height: 1200px;
    overflow: hidden;
    background:
      radial-gradient(ellipse 65% 55% at 88% 28%, var(--sky-gold) 0%, transparent 75%),
      linear-gradient(135deg, var(--sky-purple) 0%, var(--sky-mauve) 38%, var(--sky-amber) 75%, var(--sky-gold) 100%);
  }
  .saxophone-photo {
    position: absolute;
    inset: 0;
    overflow: hidden;
  }
  .saxophone-body {
    position: absolute;
    left: 150px;
    top: -120px;
    width: 370px;
    height: 1500px;
    transform: rotate(14deg);
    transform-origin: 50% 50%;
    background: linear-gradient(90deg, var(--brass-deep) 0%, var(--brass-mid) 45%, var(--brass-light) 85%, rgba(196,96,46,0) 100%);
    filter: blur(18px);
    opacity: 0.9;
  }
  .saxophone-bell {
    position: absolute;
    left: 470px;
    top: 800px;
    width: 520px;
    height: 480px;
    border-radius: 50%;
    transform: rotate(-25deg);
    background: radial-gradient(ellipse at 40% 35%, var(--brass-light) 0%, var(--brass-mid) 55%, var(--brass-deep) 100%);
    filter: blur(16px);
    opacity: 0.92;
  }
  .title-block {
    position: absolute;
    left: 460px;
    width: 480px;
    top: 405px;
    text-align: center;
    font-family: "Lilita One", sans-serif;
    font-weight: 400;
    font-size: 76px;
    line-height: 75px;
    letter-spacing: 1px;
    color: var(--title-yellow);
    text-shadow: 3px 4px 0 var(--title-shadow);
  }
  .studios {
    position: absolute;
    left: 460px;
    width: 480px;
    top: 650px;
    text-align: center;
    font-family: "Roboto Condensed", sans-serif;
    font-weight: 700;
    font-size: 25px;
    line-height: 40px;
    color: var(--info-white);
    text-shadow: 1px 1px 2px rgba(0,0,0,0.35);
  }
  .event-details {
    position: absolute;
    left: 460px;
    width: 480px;
    top: 1074px;
    text-align: center;
    font-family: "Roboto Condensed", sans-serif;
    font-weight: 700;
    font-size: 25px;
    line-height: 44px;
    color: var(--info-white);
    text-shadow: 1px 1px 2px rgba(0,0,0,0.45);
  }
</style>
</head>
<body>
<main class="poster">
  <div class="saxophone-photo" role="img" aria-label="Close-up photograph of a gold saxophone body and keys rising diagonally, with its bell at the lower right">
    <div class="saxophone-body"></div>
    <div class="saxophone-bell"></div>
  </div>

  <h1 class="title-block">Brindle<br>Saxophone<br>Ensembles</h1>

  <p class="studios">from the Studios of<br>Perry Halvorsen and Neil Dumont</p>

  <p class="event-details">Friday, April 19 at 8pm<br>Tobias Wrenfield Concert Hall</p>
</main>
</body>
</html>
```